I need a new business card design for my pharmacy.

I need a business card design. I will include my logo.
The card needs to be readable. I prefer to have my logo on one side along with my website, the other side includes the other information. Please use combination of black, neon green, white, and silver. This needs to catch the eye but yet be clearly visible and legible. Thanks

Industry/Entity Type

Pharmacy

Contact Information for Business Card

It needs to have the following information listed:
Mel's Apothecary Owner/Pharm D.
7134 North Brook Lane
Sioux Falls, SD 57231
Phone 605-318-6207
Fax 605-318-6209
email: mel@melsapothecary-example.com
www.melsapothecary-example.com
Store hours Monday-Friday 8 am- 7 pm
Saturday 8 am- 12 pm
Sunday Closed
Please utilize the colors black, white, and neon green, maybe silver.

Requirements
Must have
• It needs to be easily readable!
Nice to have
• It should catch the eye.
Should not have
• Do not use any other colors except listed: black, neon green, white, & silver.

```html
<!DOCTYPE html>
<html lang="en">
<head>
<meta charset="utf-8">
<title>Mel's Apothecary – Business Card Front</title>
<link rel="stylesheet" href="https://fonts.googleapis.com/css2?family=Source+Sans+3:wght@400;600&display=swap">
<style>
  :root {
    --ink: #1c1b1c;
    --neon-green: #9ccc3c;
    --silver-light: #eeeff2;
    --silver-mid: #e2e3e7;
    --silver-deep: #d6d7dc;
  }
  * { margin: 0; padding: 0; box-sizing: border-box; }
  html, body {
    width: 1200px;
    height: 667px;
    overflow: hidden;
    background: var(--silver-light);
  }
  .card {
    position: relative;
    width: 1200px;
    height: 667px;
    overflow: hidden;
    font-family: "Source Sans 3", sans-serif;
  }
  .card__pattern {
    position: absolute;
    inset: 0;
    background: linear-gradient(135deg, var(--silver-light) 0%, var(--silver-mid) 45%, var(--silver-light) 70%, var(--silver-deep) 100%);
  }
  .brand {
    position: absolute;
    left: 150px;
    top: 192px;
    height: 172px;
    display: flex;
    align-items: center;
  }
  .brand__dot {
    width: 110px;
    height: 110px;
    border-radius: 50%;
    background: var(--neon-green);
    flex: none;
  }
  .brand__divider {
    width: 3px;
    height: 172px;
    background: var(--ink);
    margin: 0 46px 0 93px;
    flex: none;
  }
  .brand__name {
    font-weight: 600;
    font-size: 77px;
    letter-spacing: -1.5px;
    color: var(--ink);
    white-space: nowrap;
    line-height: 1;
  }
  .website {
    position: absolute;
    left: 0;
    width: 1180px;
    top: 462px;
    text-align: center;
    font-weight: 400;
    font-size: 50px;
    color: var(--neon-green);
    letter-spacing: 0.5px;
    line-height: 1;
  }
</style>
</head>
<body>
  <main class="card">
    <div class="card__pattern" role="img" aria-label="Soft silver geometric cube pattern background"></div>
    <div class="brand">
      <span class="brand__dot"></span>
      <span class="brand__divider"></span>
      <h1 class="brand__name">Mel's Apothecary</h1>
    </div>
    <p class="website">www.melsapothecary-example.com</p>
  </main>
</body>
</html>
```